Research Flier

I need to take a very bad flier that I made and turn it into an amazing flyer for my research group to be shared at a high profile conference.

```html
<!DOCTYPE html>
<html lang="en">
<head>
<meta charset="utf-8">
<title>The Kindness Lab – Research Flier</title>
<link href="https://fonts.googleapis.com/css2?family=Roboto:wght@400;500;700;900&family=Roboto+Slab:wght@500;600&display=swap" rel="stylesheet">
<style>
:root{
  --green:#8cc63f;
  --orange:#e05a2b;
  --ink:#222222;
  --navy:#1e2f5c;
  --grey:#666a70;
  --soft-grey:#9aa3ab;
  --line:#e9a08a;
  --paper:#ffffff;
  --bg:#ffffff;
}
*{box-sizing:border-box;margin:0;padding:0}
html,body{width:1200px;height:1200px;overflow:hidden;background:var(--bg)}
body{position:relative;font-family:"Roboto",Arial,sans-serif;color:var(--ink)}
.page{position:absolute;top:240px;width:540px;height:722px;background:var(--paper);overflow:hidden;outline:1px solid #eeeeee}
.front{left:40px}
.back{left:620px}
.abs{position:absolute}

/* FRONT */
.hero{left:0;top:0;width:540px;height:140px;background:linear-gradient(100deg,#e9e4dc 0%,#c9d3de 45%,#d7c08c 60%,#9aa7b6 100%)}
.hero-title{left:12px;top:12px;width:200px;font-family:"Roboto Slab",Georgia,serif;font-weight:600;font-size:15.5px;line-height:16.5px;color:var(--navy);text-align:center}
.band{left:0;top:140px;width:540px;height:17px;background:var(--green)}
.lab-name{left:110px;top:139px;width:321px;height:41px;background:var(--orange);color:#fff;font-weight:900;font-size:22px;display:flex;align-items:center;justify-content:center;letter-spacing:.2px}
.mission-head{left:48px;top:196px;font-weight:900;font-size:19px;color:var(--orange)}
.mission-list{left:34px;top:232px;width:470px;list-style:none}
.mission-list li{position:relative;padding-left:28px;font-size:14px;line-height:20.3px;margin-bottom:11.5px}
.mission-list li::before{content:"";position:absolute;left:4px;top:4px;width:12px;height:12px;border-radius:50%;background:var(--orange)}
.photo-left{left:0;top:469px;width:279px;height:140px;background:linear-gradient(180deg,#c8c2c9 0%,#8f7f86 60%,#bfb6a8 100%)}
.photo-right{left:283px;top:469px;width:255px;height:140px;background:linear-gradient(160deg,#3a3d3a 0%,#b8433c 55%,#d94a3c 100%)}
.footer-front{left:0;top:630px;width:540px;height:80px;display:flex;align-items:center;justify-content:space-between;padding:0 26px}
.program-name{font-size:24px;font-weight:400;color:var(--grey);letter-spacing:1px}
.divider{width:1px;height:54px;background:#999}
.partner-badge{width:30px;height:30px;background:#d6d9dc}
.center-name{width:150px;font-size:10px;line-height:13px;font-weight:400;color:var(--grey)}

/* BACK */
.change-box{left:0;top:19px;width:151px;height:80px}
.change-box span{position:absolute;left:0;top:0;width:140px;height:80px;display:flex;align-items:center;justify-content:center;text-align:center;color:#fff;font-weight:700;font-size:14px;line-height:18px}
.change-head{left:162px;top:9px;font-weight:700;font-size:11.5px;color:var(--orange)}
.change-list{left:162px;top:28px;width:360px;font-size:8.8px;line-height:11px;list-style:none}
.change-list li{margin-bottom:6px}
.site{position:absolute;width:73px;height:42px;border:1px solid var(--line);border-radius:3px;padding:7px 4px 2px 5px}
.site b{position:absolute;left:5px;top:-5px;height:8px;padding:0 6px;background:var(--green);color:#fff;font-size:5px;line-height:8px;border-radius:2px}
.site ul{padding-left:7px;font-size:4.3px;line-height:5.2px;color:#333}
.wheel-label{position:absolute;width:150px;font-size:6.2px;line-height:8px;color:#555}
.wheel-label h4{font-size:9.5px;font-weight:500;margin-bottom:3px}
.left-lab{text-align:right}
.c-orange{color:var(--orange)}
.c-green{color:#6fa52a}
.c-navy{color:var(--navy)}
.c-grey{color:var(--grey)}
.assess-bar{left:16px;top:445px;width:502px;height:17px;background:var(--orange);color:#fff;font-weight:700;font-size:13px;text-align:center;line-height:17px}
.proj{position:absolute;top:475px;font-size:6.4px;line-height:8.6px;color:#222}
.proj a{color:var(--orange);text-decoration:underline}
.proj-img{position:absolute;top:478px;background:linear-gradient(135deg,#eef0f2,#c9cfd6)}
.col-rule{position:absolute;top:468px;width:1px;height:68px;background:var(--orange)}
.sub-head{position:absolute;font-size:8.4px;font-weight:500;color:var(--green);text-decoration:underline}
.small-list{position:absolute;font-size:5px;line-height:6.3px;color:#333;padding-left:14px}
.small-list li{margin-bottom:4px}
.pubs{position:absolute;left:236px;top:572px;width:290px;font-size:4.5px;line-height:5.6px;color:#333}
.pubs p{margin-bottom:3.5px}
.pubs i{font-style:italic}
.back-brand{left:22px;top:682px;display:flex;align-items:center;gap:14px}
.back-brand .program-name{font-size:13px}
.back-brand .partner-badge{width:22px;height:22px}
.vrule{left:229px;top:555px;width:1px;height:148px;background:var(--orange)}
</style>
</head>
<body>

<section class="page front">
  <div class="abs hero" role="img" aria-label="Photo of a panel discussion on stage in front of a colourful world map"></div>
  <h1 class="abs hero-title">HEART Learning:<br>A Worldwide Initiative<br>for Educating the<br>Heart and Mind</h1>
  <div class="abs band"></div>
  <div class="abs lab-name">THE KINDNESS LAB</div>

  <h2 class="abs mission-head">MISSION</h2>
  <ul class="abs mission-list">
    <li>Supporting the development of the evidence-based, HEART Learning program and MCT for Educators by assessing program implementation and examining feasibility, impact, and long-term sustainability at the school, district, city, and national levels.</li>
    <li>Developing effective tools and measures to MCT and HEART Learning</li>
    <li>Support global dissemination through impactful manualization</li>
    <li>Contribute to compassion-based education studies worldwide through scientific advancements that examine compassion, common humanity, wellbeing, interdependence, and secular ethics.</li>
  </ul>

  <div class="abs photo-left" role="img" aria-label="Group photo of educators holding certificates in a school gym"></div>
  <div class="abs photo-right" role="img" aria-label="Photo of students in red uniforms around a box in a classroom"></div>

  <div class="abs footer-front">
    <p class="program-name">HEART LEARNING</p>
    <div class="divider"></div>
    <div class="partner-badge" role="img" aria-label="Partner badge"></div>
    <p class="center-name">Center for Mindful Science and Care-Based Ethics, Ridgewell University</p>
  </div>
</section>

<section class="page back">
  <div class="abs change-box">
    <svg width="151" height="80" viewBox="0 0 151 80"><polygon points="0,0 140,0 151,40 140,80 0,80" fill="#8cc63f"/></svg>
    <span>BUILDING<br>FOR CHANGE</span>
  </div>
  <h3 class="abs change-head">To meaningfully impact change, we have:</h3>
  <ul class="abs change-list">
    <li>Identified seven critical domains for whole-school implementation sustainment</li>
    <li>Conducted studies on sustainable implementation and its impact on compassionate systems</li>
    <li>Begun work on global implementation frameworks, monitoring guides, and whole-school trainings</li>
  </ul>

  <div class="site" style="left:20px;top:127px"><b>USA</b><ul><li>Several studies, late elementary</li><li>Multiple districts</li><li>RCT &amp; mixed methods</li></ul></div>
  <div class="site" style="left:105px;top:127px"><b>Sweden</b><ul><li>Late Elementary</li><li>2 Schools</li><li>Feasibility &amp; Qualitative Impact Study</li></ul></div>
  <div class="site" style="left:190px;top:127px"><b>Spain</b><ul><li>Late Elementary</li><li>Multiple Schools Across Two Regions</li><li>Implementation Study</li></ul></div>
  <div class="site" style="left:275px;top:127px"><b>Ukraine</b><ul><li>Teachers</li><li>Feasibility &amp; Qualitative Impact Study</li></ul></div>
  <div class="site" style="left:360px;top:127px"><b>Mongolia</b><ul><li>Late Elementary to High School</li><li>800+ Students</li><li>6 Schools</li><li>Implementation study</li></ul></div>
  <div class="site" style="left:445px;top:127px"><b>Mexico</b><ul><li>Pre-service Course Study</li><li>Feasibility and Preliminary Impact</li><li>Mexico</li></ul></div>
  <div class="site" style="left:20px;top:182px"><b>Colombia</b><ul><li>Late Elementary</li><li>300+ students</li><li>Implementation Study</li><li>Feasibility &amp; Qualitative</li></ul></div>
  <div class="site" style="left:105px;top:182px"><b>Brazil</b><ul><li>Late Elementary</li><li>Ten Schools</li><li>Randomized Controlled Trial</li><li>Teachers &amp; Students</li></ul></div>
  <div class="site" style="left:190px;top:182px"><b>Kenya</b><ul><li>Late Elementary</li><li>2 Schools</li><li>Feasibility &amp; Qualitative Impact Study</li></ul></div>
  <div class="site" style="left:275px;top:182px"><b>India</b><ul><li>Late Elementary</li><li>More than 1300 Students</li><li>Urban and Rural studies</li><li>Case Studies</li></ul></div>
  <div class="site" style="left:360px;top:182px"><b>South Korea</b><ul><li>Elementary</li><li>Implementation Study</li></ul></div>
  <div class="site" style="left:445px;top:182px"><b>Vietnam</b><ul><li>Feasibility</li><li>Implementation in Elementary Students</li><li>Preliminary Impact</li></ul></div>

  <svg class="abs" style="left:180px;top:252px" width="180" height="180" viewBox="0 0 180 180" role="img" aria-label="Donut chart of seven equal implementation domains">
    <g transform="rotate(-90 90 90)" fill="none" stroke-width="44">
      <circle cx="90" cy="90" r="56" stroke="#1e2f5c" stroke-dasharray="48.3 303.6" stroke-dashoffset="0"/>
      <circle cx="90" cy="90" r="56" stroke="#e05a2b" stroke-dasharray="48.3 303.6" stroke-dashoffset="-50.27"/>
      <circle cx="90" cy="90" r="56" stroke="#8cc63f" stroke-dasharray="48.3 303.6" stroke-dashoffset="-100.54"/>
      <circle cx="90" cy="90" r="56" stroke="#666a70" stroke-dasharray="48.3 303.6" stroke-dashoffset="-150.81"/>
      <circle cx="90" cy="90" r="56" stroke="#e9a08a" stroke-dasharray="48.3 303.6" stroke-dashoffset="-201.08"/>
      <circle cx="90" cy="90" r="56" stroke="#b9dc8c" stroke-dasharray="48.3 303.6" stroke-dashoffset="-251.35"/>
      <circle cx="90" cy="90" r="56" stroke="#9aa3ab" stroke-dasharray="48.3 303.6" stroke-dashoffset="-301.62"/>
    </g>
  </svg>

  <div class="wheel-label left-lab" style="left:18px;top:262px"><h4 class="c-navy">Implementation</h4>Take an implementation approach that works for your school based on what works</div>
  <div class="wheel-label left-lab" style="left:18px;top:313px"><h4 class="c-orange">Implementation</h4>Take an implementation approach that works for your school based on what works</div>
  <div class="wheel-label left-lab" style="left:18px;top:364px"><h4 class="c-grey">Community Engagement</h4>Engaging families and communities creates a shared vision that enhances sustainability</div>
  <div class="wheel-label" style="left:365px;top:253px"><h4 class="c-orange">Student Voice</h4>Student voice and inclusion is developing HEART creates opportunities of stronger program impact</div>
  <div class="wheel-label" style="left:365px;top:300px"><h4 class="c-navy">District Initiative Alignment</h4>HEART must align with school initiatives as a part of shared goals that are communicated</div>
  <div class="wheel-label" style="left:365px;top:346px"><h4 class="c-green">Adult SEL</h4>Professional development includes SEL for adults to create supportive schools</div>
  <div class="wheel-label" style="left:365px;top:386px"><h4 class="c-green">Communities of Practice</h4>Ongoing professional development support creates opportunities and spaces to strengthen educator development</div>

  <div class="abs assess-bar">Assessment Development Projects</div>
  <svg class="abs" style="left:0;top:461px" width="540" height="10"><polygon points="72,0 86,0 79,9" fill="#8cc63f"/><polygon points="242,0 256,0 249,9" fill="#8cc63f"/><polygon points="411,0 425,0 418,9" fill="#8cc63f"/></svg>
  <div class="proj-img" style="left:20px;top:478px;width:46px;height:42px" role="img" aria-label="Sketch of assessment worksheets"></div>
  <p class="proj" style="left:71px;width:90px"><a>Digital Assessment: HEART Learning Insight</a> - curriculum-based assessment tool being developed in collaboration with Lumora</p>
  <div class="col-rule" style="left:165px"></div>
  <p class="proj" style="left:175px;width:135px"><a>Developmentally Appropriate Expectations of Change:</a> We are building age-appropriate rubrics that span the K-12 curriculum. They will help teachers understand expected changes in behavior, communication, relationships, and learning.</p>
  <div class="col-rule" style="left:323px"></div>
  <div class="proj-img" style="left:333px;top:478px;width:55px;height:48px" role="img" aria-label="Grid of small assessment icons"></div>
  <p class="proj" style="left:395px;width:125px"><a>Assessment Package for Framework-Based Effectiveness:</a> With affiliates, development of an assessment package for effectiveness studies aimed at assessing domain components, specific to our programs.</p>

  <div class="abs vrule"></div>
  <h4 class="sub-head" style="left:15px;top:558px">Other Key Areas of Development</h4>
  <ul class="small-list" style="left:22px;top:572px;width:205px">
    <li>Global Implementation Framework: Establishing a foundation for a monitoring and evaluation approach that is informed and grounded by practices worldwide to better support implementation.</li>
    <li>Whole School/System Trainings and Courses: Utilizing theories for comprehensive school-wide and system-wide implementation to address the sustainability of HEART Learning and SEL programs.</li>
  </ul>
  <h4 class="sub-head" style="left:15px;top:634px">Student Team</h4>
  <ul class="small-list" style="left:22px;top:648px;width:205px">
    <li>Currently, over 38 undergraduates, masters students, and PhD students from Ridgewell and globally have been a part of our student research team.</li>
  </ul>
  <div class="abs back-brand"><p class="program-name">HEART LEARNING</p><div class="partner-badge" role="img" aria-label="Partner badge"></div></div>

  <h4 class="sub-head" style="left:236px;top:558px">Key Publications</h4>
  <div class="pubs">
    <p>US: Author, A., Writer, B. (2024). Cultivating compassion in classroom settings: a school-based program study. <i>Journal of Education. In review.</i></p>
    <p>Colombia: Author, A., Writer, C. (2024). Resilience and renewal in elementary schools through social and ethical learning. <i>In review.</i></p>
    <p>South Korea: Author, D., Writer, E. (2024). Building resilience and social competencies through a short-term program. <i>Behavioral Studies.</i></p>
    <p>Ukraine: Author, F., Writer, G. (2024). Effects of a school-based program on student well-being in times of conflict. <i>In review.</i></p>
    <p>Brazil: Author, H., Writer, I. (2024). Mental health improvements of a four-week ethical learning course for teachers. <i>In review.</i></p>
    <p>Mongolia: Author, J., Writer, K. (2024). Predicting happiness and life satisfaction of middle school students. <i>Educational Studies.</i></p>
    <p>Global: Author, L., Writer, M. (2023). Nurturing positive mental health in educational settings. <i>Public Health.</i></p>
  </div>
</section>

</body>
</html>
```